Velborne Systems needs a business card

The logo we have uploaded is going to be the image centered on the back.
The business card color is going to be black. Increase the contrast in the logo and lettering so the grey stands out from the black and is more readable. Keep the shadow effect if you can.
On the front, the only part of the logo that should be used is the Egyptian character. We would like the following information included: Name (first last), Title, Phone number, email and company name (Velborne Systems).
The images of colored sound waves we uploaded is a concept we would like implemented on the front as well but please do not use the exact image. It is for guideline purposes.
Get creative with the empty space. We are a technology company that deals with sound and lights. Please not too busy.
Thank you, we look forward to all your submissions.

```html
<!DOCTYPE html>
<html lang="en">
<head>
<meta charset="utf-8">
<title>Velborne Systems – Business Card</title>
<link href="https://fonts.googleapis.com/css2?family=Audiowide&family=Exo+2:wght@400;600;700&display=swap" rel="stylesheet">
<style>
  :root {
    --canvas: #e9e4da;
    --card: #2a2a2b;
    --card-deep: #222223;
    --red: #e8323b;
    --grey: #8d8d90;
    --grey-light: #c9c9cc;
    --white: #ffffff;
  }
  * { box-sizing: border-box; margin: 0; padding: 0; }
  html, body {
    width: 1057px; height: 1200px; overflow: hidden;
    background: var(--canvas);
    font-family: "Exo 2", sans-serif;
  }
  .sheet {
    width: 1057px; height: 1200px;
    display: flex; flex-direction: column; align-items: center; justify-content: center;
    gap: 60px;
  }
  .card {
    position: relative;
    width: 900px; height: 514px;
    background: var(--card);
    overflow: hidden;
    box-shadow: 0 10px 30px rgba(0,0,0,.25);
  }
  /* Back */
  .card-back { border: 18px solid var(--grey); }
  .card-back .frame {
    position: absolute; inset: 0;
    border: 14px solid var(--red);
    display: flex; align-items: center; justify-content: center;
  }
  .brand { display: flex; align-items: center; gap: 26px; }
  .brand-square { width: 70px; height: 70px; background: var(--red); }
  .brand-name {
    font-family: "Audiowide", sans-serif;
    font-size: 58px; color: var(--grey-light); letter-spacing: 2px;
    line-height: 1;
  }
  /* Front */
  .card-front .shapes { position: absolute; inset: 0; }
  .front-figure {
    position: absolute; left: 360px; top: 40px;
    width: 90px; height: 130px;
    background: linear-gradient(180deg, #5a5a5d, #c92f36);
    border-radius: 6px;
  }
  .front-brand {
    position: absolute; left: 470px; top: 110px;
    font-family: "Audiowide", sans-serif;
    font-size: 40px; color: var(--grey-light); letter-spacing: 1px;
  }
  .identity {
    position: absolute; left: 60px; top: 338px; color: var(--white);
  }
  .identity .name {
    font-family: "Audiowide", sans-serif; font-size: 34px; letter-spacing: 2px;
  }
  .identity .title { font-size: 20px; letter-spacing: 4px; margin-top: 4px; }
  .contacts {
    position: absolute; left: 60px; top: 425px;
    list-style: none; color: var(--white); font-size: 16px;
  }
  .contacts li, .phones li { display: flex; align-items: center; gap: 12px; height: 27px; }
  .icon {
    width: 20px; height: 20px; background: var(--white);
    display: flex; align-items: center; justify-content: center; flex: none;
  }
  .phones {
    position: absolute; left: 640px; top: 290px;
    list-style: none; color: var(--white); font-size: 17px; letter-spacing: 1px;
  }
</style>
</head>
<body>
<main class="sheet">

  <section class="card card-back" aria-label="Card back">
    <div class="frame">
      <div class="brand">
        <span class="brand-square"></span>
        <span class="brand-name">VELBORNE SYSTEMS</span>
      </div>
    </div>
  </section>

  <section class="card card-front" aria-label="Card front">
    <svg class="shapes" width="900" height="514" viewBox="0 0 900 514">
      <defs>
        <linearGradient id="band-grey" x1="0" y1="1" x2="1" y2="0">
          <stop offset="0" stop-color="#4a4a4d"/>
          <stop offset=".5" stop-color="#b5b5b8"/>
          <stop offset="1" stop-color="#5c5c5f"/>
        </linearGradient>
      </defs>
      <polygon points="430,514 560,514 900,200 900,70" fill="url(#band-grey)"/>
      <polygon points="560,514 600,514 900,237 900,200" fill="#3a3a3c"/>
      <polygon points="0,310 545,310 440,514 0,514" fill="var(--red)"/>
      <polygon points="0,410 493,410 440,514 0,514" fill="var(--card-deep)" opacity=".55"/>
    </svg>

    <div class="front-figure" role="img" aria-label="Brand figure illustration"></div>
    <div class="front-brand">VELBORNE SYSTEMS</div>

    <div class="identity">
      <div class="name">MARCUS REYL</div>
      <div class="title">FOUNDER</div>
    </div>

    <ul class="contacts">
      <li><span class="icon"><svg width="12" height="12" viewBox="0 0 12 12"><path d="M6 1a3.5 3.5 0 0 0-3.5 3.5C2.5 7.5 6 11 6 11s3.5-3.5 3.5-6.5A3.5 3.5 0 0 0 6 1z" fill="#e8323b"/></svg></span>2240 Orchard Lane, Suite 5, Ridgefield</li>
      <li><span class="icon"><svg width="12" height="12" viewBox="0 0 12 12"><circle cx="6" cy="6" r="4.5" fill="none" stroke="#e8323b" stroke-width="1.4"/><path d="M1.5 6h9M6 1.5v9" stroke="#e8323b" stroke-width="1"/></svg></span>www.velbornesystems.com</li>
      <li><span class="icon"><svg width="12" height="12" viewBox="0 0 12 12"><rect x="1" y="2.5" width="10" height="7" fill="none" stroke="#e8323b" stroke-width="1.4"/><path d="M1 2.5l5 4 5-4" fill="none" stroke="#e8323b" stroke-width="1.2"/></svg></span>marcus@velbornesystems.com</li>
    </ul>

    <ul class="phones">
      <li><span class="icon"><svg width="12" height="12" viewBox="0 0 12 12"><path d="M3 1l2 2.5-1 1.2a7 7 0 0 0 3.3 3.3l1.2-1L11 9l-1.5 2C5 11 1 7 1 2.5z" fill="#2a2a2b"/></svg></span>014 552 0193</li>
      <li><span class="icon"><svg width="12" height="12" viewBox="0 0 12 12"><rect x="3" y="1" width="6" height="10" rx="1" fill="#2a2a2b"/></svg></span>014 552 0194</li>
    </ul>
  </section>

</main>
</body>
</html>
```